Veltrano - Mechanic/Collision Center Business Card

We're looking for a business card design for our mechanic/ collision repair shop.

Can be with colours or monochromatic.

See the attached files.

Many thanks

```html
<!DOCTYPE html>
<html lang="en">
<head>
<meta charset="utf-8">
<title>Veltrano – Business Card</title>
<link rel="stylesheet" href="https://fonts.googleapis.com/css2?family=Arimo:wght@400;700&display=swap">
<style>
  :root {
    --backdrop: #2e2e2e;
    --card: #ffffff;
    --ink: #14181b;
    --muted: #77797c;
    --accent: #1e9cd7;
    --rule: #3a3d40;
  }
  * { margin: 0; padding: 0; box-sizing: border-box; }
  html, body {
    width: 1200px; height: 1200px; overflow: hidden;
    background: var(--backdrop);
    font-family: "Arimo", Arial, sans-serif;
  }
  .canvas { position: relative; width: 1200px; height: 1200px; }
  .card {
    position: absolute; left: 170px; width: 860px; height: 491px;
    background: var(--card);
  }
  .card--front { top: 80px; }
  .card--back { top: 630px; }

  .brand {
    position: absolute; display: flex; align-items: center; gap: 18px;
  }
  .brand__dot {
    width: 54px; height: 54px; border-radius: 50%; background: var(--accent);
  }
  .brand__name {
    font-weight: 700; color: var(--ink); letter-spacing: 2px;
  }
  .card--front .brand { left: 50%; top: 50%; transform: translate(-50%, -50%); }
  .card--front .brand__name { font-size: 74px; }
  .card--back .brand { right: 70px; top: 95px; }
  .card--back .brand__dot { width: 42px; height: 42px; }
  .card--back .brand__name { font-size: 56px; }

  .company {
    position: absolute; left: 62px; top: 240px; font-size: 17px; line-height: 1.3;
  }
  .company__name { color: var(--ink); font-weight: 700; font-size: 19px; }
  .company__address { color: var(--muted); }
  .contact-list { list-style: none; margin-top: 16px; color: #3b3d40; }
  .contact-list li { display: flex; align-items: center; gap: 10px; margin-bottom: 4px; }
  .icon { width: 16px; height: 16px; flex: none; fill: var(--accent); }

  .divider {
    position: absolute; left: 408px; top: 330px; width: 1px; height: 110px;
    background: var(--rule);
  }
  .person { position: absolute; left: 440px; top: 340px; line-height: 1.25; }
  .person__name { color: var(--ink); font-size: 21px; }
  .person__role { color: var(--muted); font-size: 22px; }
  .person__phone { display: flex; align-items: center; gap: 10px; margin-top: 8px; font-size: 18px; color: #3b3d40; }
</style>
</head>
<body>
<main class="canvas">
  <section class="card card--front">
    <div class="brand">
      <span class="brand__dot"></span>
      <span class="brand__name">VELTRANO</span>
    </div>
  </section>

  <section class="card card--back">
    <div class="brand">
      <span class="brand__dot"></span>
      <span class="brand__name">VELTRANO</span>
    </div>

    <div class="company">
      <p class="company__name">Veltrano, LDA</p>
      <p class="company__address">Rua das Oficinas, 42</p>
      <p class="company__address">1200-310 Lisboa(Postal code)</p>
      <ul class="contact-list">
        <li>
          <svg class="icon" viewBox="0 0 16 16"><path d="M4 1l3 3-2 2c1 2 3 4 5 5l2-2 3 3-2 3C7 15 1 9 1 3z"/></svg>
          +351 210555184
        </li>
        <li>
          <svg class="icon" viewBox="0 0 16 16"><path d="M1 3h14v10H1z M2 4l6 5 6-5" fill="none" stroke="#1e9cd7" stroke-width="1.6"/></svg>
          veltrano.oficina@mail.com
        </li>
        <li>
          <svg class="icon" viewBox="0 0 16 16"><circle cx="8" cy="8" r="7"/></svg>
          www.veltrano-auto.pt
        </li>
      </ul>
    </div>

    <div class="divider"></div>

    <div class="person">
      <p class="person__name">Tomás Ferreira</p>
      <p class="person__role">Manager</p>
      <p class="person__phone">
        <svg class="icon" viewBox="0 0 16 16"><path d="M4 1l3 3-2 2c1 2 3 4 5 5l2-2 3 3-2 3C7 15 1 9 1 3z"/></svg>
        +351 910555247
      </p>
    </div>
  </section>
</main>
</body>
</html>
```